Looking for a professional, clean and crisp business card

I am in the underground utilities industry and am just looking for a really impressive business card. I would like our card to be white with our symbol crisp and clear with it protruding. I also have a business partner that will require his name and info on the card once the design is set. I would like to have our website info on the card which is;
http://granitetrenchco.example/

Contact Information for Business Card

Website, contact name, number and email

```html
<!DOCTYPE html>
<html lang="en">
<head>
<meta charset="UTF-8">
<title>Granite Trench Co — Business Card</title>
<link rel="stylesheet" href="https://fonts.googleapis.com/css2?family=Oswald:wght@600&family=Montserrat:wght@400&display=swap">
<style>
  :root {
    --page-bg: #1f1f21;
    --card-black: #070708;
    --card-charcoal: #16181b;
    --card-white: #ffffff;
    --brand-blue: #3a5fa8;
    --ink-light: #ffffff;
    --ink-dark: #0b0b0c;
  }
  * { margin: 0; padding: 0; box-sizing: border-box; }
  html, body { width: 1200px; height: 900px; overflow: hidden; background: var(--page-bg); }
  .stage { position: relative; width: 1200px; height: 900px; }
  .card {
    position: absolute; left: 270px; width: 660px; height: 377px;
    overflow: hidden; box-shadow: 0 10px 30px rgba(0,0,0,.55);
  }
  .card-back { top: 55px; background: var(--card-black); }
  .card-front { top: 468px; background: var(--card-white); }

  .back-texture {
    position: absolute; inset: 0;
    background: linear-gradient(135deg, var(--card-charcoal) 0%, #0c0d0f 55%, var(--card-black) 100%);
  }
  .brand-mark {
    position: absolute; display: flex; align-items: center; gap: 12px;
    font-family: "Oswald", sans-serif; font-weight: 600; text-transform: uppercase;
    letter-spacing: 1px; line-height: 1;
  }
  .brand-mark .dot { width: 22px; height: 22px; border-radius: 50%; }
  .card-back .brand-mark { right: 40px; top: 168px; color: var(--ink-light); font-size: 30px; }
  .card-back .brand-mark .dot { background: var(--ink-light); }
  .card-front .brand-mark { left: 36px; top: 100px; color: var(--ink-dark); font-size: 32px; }
  .card-front .brand-mark .dot { background: var(--ink-dark); }

  .swoosh { position: absolute; inset: 0; }

  .contact-block { position: absolute; right: 34px; bottom: 20px; text-align: right; }
  .person-name {
    font-family: "Oswald", sans-serif; font-weight: 600; font-size: 27px; line-height: 1.1;
    letter-spacing: 1px; color: var(--ink-light); text-transform: uppercase; margin-bottom: 8px;
  }
  .contact-line {
    display: flex; justify-content: flex-end; align-items: center; gap: 10px;
    font-family: "Montserrat", sans-serif; font-size: 17px; color: var(--ink-light);
    line-height: 1.55;
  }
  .contact-line .accent { color: var(--brand-blue); }
  .contact-line svg { width: 20px; height: 20px; flex: none; }
</style>
</head>
<body>
<main class="stage">
  <section class="card card-back" aria-label="Card back">
    <div class="back-texture" role="img" aria-label="Dark pattern of diagonal black pipes"></div>
    <div class="brand-mark"><span class="dot"></span>Granite Trench Co</div>
  </section>

  <section class="card card-front" aria-label="Card front">
    <svg class="swoosh" viewBox="0 0 660 377" width="660" height="377" aria-hidden="true">
      <path d="M0,215 C30,335 330,300 620,104 L660,104 L660,377 L0,377 Z" fill="var(--brand-blue)"/>
      <path d="M0,316 C220,323 470,223 660,112 L660,377 L0,377 Z" fill="var(--card-white)"/>
      <path d="M0,323 C220,330 470,230 660,120 L660,377 L0,377 Z" fill="var(--card-black)"/>
    </svg>
    <div class="brand-mark"><span class="dot"></span>Granite Trench Co</div>

    <div class="contact-block">
      <p class="person-name">Dale Morrow</p>
      <p class="contact-line">604-555-0148
        <svg viewBox="0 0 24 24" fill="none" stroke="var(--brand-blue)" stroke-width="1.8"><circle cx="12" cy="12" r="10"/><path d="M8.5 7.5c.5 3.5 3 6.5 7 8l1.5-1.8-2.2-1.2-1 1c-1.5-.7-2.6-1.8-3.2-3.3l1-1-1.1-2.2z"/></svg>
      </p>
      <p class="contact-line">dale@granitetrenchco.example
        <svg viewBox="0 0 24 24" fill="none" stroke="var(--brand-blue)" stroke-width="1.8"><rect x="2.5" y="5" width="19" height="14"/><path d="M2.5 5l9.5 8 9.5-8"/></svg>
      </p>
      <p class="contact-line"><span>www.<span class="accent">granitetrenchco</span>.example</span>
        <svg viewBox="0 0 24 24" fill="none" stroke="var(--brand-blue)" stroke-width="1.8"><circle cx="12" cy="12" r="10"/><path d="M2 12h20M12 2c3 3 3 17 0 20M12 2c-3 3-3 17 0 20M4 7h16M4 17h16"/></svg>
      </p>
    </div>
  </section>
</main>
</body>
</html>
```